Substack Newsletter design, branding, logo, images

I'm designing my Substack newsletter. I'm a creative- writer and artist. It needs to feature that, and express that my newsletter will be about inspiring other creatives and storytellers, writing about my journey as a storyteller, sharing writing advice and uploading short stories, and images of my comics and art. That's the asthetic design. I'll need images for cover banner, welcome pages, wordmark (stylized image version of my newsletter publication name) email banner, and more. A total set up for my newsletter. I've included images from my old Wordpress design to give indications of what we'll be thinking of.

```html
<!DOCTYPE html>
<html lang="en">
<head>
<meta charset="utf-8">
<title>Inkvale Reads</title>
<link href="https://fonts.googleapis.com/css2?family=Lexend:wght@500;600&family=Roboto:wght@400&display=swap" rel="stylesheet">
<style>
:root{
  --ink:#33295f;
  --band:#3a2f6c;
  --footer:#231b47;
  --rule:#c4c2d2;
  --hero-top:#c9d1f7;
  --hero-bottom:#d6defa;
  --text:#2a2a2a;
  --white:#ffffff;
  --tile-border:#d7d7de;
}
*{margin:0;padding:0;box-sizing:border-box}
html,body{width:1200px;height:3672px;overflow:hidden;background:var(--white)}
body{position:relative;font-family:'Roboto',sans-serif;color:var(--text)}
.abs{position:absolute}
.hero{left:0;top:0;width:1200px;height:628px;
  background:radial-gradient(circle at 50% 0%,#e3e8fd 0%,var(--hero-top) 55%,var(--hero-bottom) 100%)}
.brand-small{left:90px;top:70px;font-family:'Lexend',sans-serif;font-weight:500;font-size:30px;color:var(--ink);letter-spacing:1px}
.brand-small .dot{display:inline-block;width:14px;height:14px;background:var(--ink);border-radius:50%;margin-right:10px;vertical-align:middle}
.wordmark{left:390px;top:105px;width:682px;text-align:center;font-family:'Lexend',sans-serif;font-weight:500;font-size:96px;color:var(--ink);line-height:1}
.hero-frame{left:474px;top:300px;width:740px;height:398px;border:4px solid var(--ink)}
.photo{background:linear-gradient(135deg,#1d4f7a,#c8502c 45%,#2a6fa0 70%,#e08a3a)}
.hero-photo{left:492px;top:315px;width:708px;height:400px}
.shadow{background:var(--ink)}
.rule{height:4px;background:var(--rule)}
h2{font-family:'Lexend',sans-serif;font-weight:600;font-size:45px;color:var(--ink);line-height:1.1}
.body-copy{font-size:17.5px;line-height:36px}
.about-shadow{left:93px;top:810px;width:435px;height:408px}
.about-photo{left:105px;top:796px;width:436px;height:409px;background:linear-gradient(160deg,#d9d2c6,#8c7d6c 50%,#5b6f8e)}
.about-rule{left:610px;top:802px;width:385px}
.about-title{left:610px;top:818px}
.about-text{left:610px;top:878px;width:494px}
.stories-rule{left:95px;top:1313px;width:385px}
.stories-title{left:95px;top:1330px}
.stories-text{left:95px;top:1390px;width:493px}
.stories-shadow{left:670px;top:1321px;width:435px;height:409px}
.stories-photo{left:657px;top:1308px;width:435px;height:410px;background:linear-gradient(150deg,#bcd3cc,#e9e1d2 45%,#e07a3a 75%,#5d8fa3)}
.advice-band{left:0;top:1813px;width:1200px;height:422px;background:var(--band)}
.advice-title{left:0;top:1868px;width:1200px;text-align:center;color:var(--white)}
.advice-text{left:126px;top:1933px;width:948px;text-align:center;color:var(--white)}
.advice-photo{left:90px;top:2122px;width:1014px;height:515px;border-radius:6px;background:linear-gradient(110deg,#c23a2e,#f08a2a 35%,#e9b07a 50%,#2c6aa8 75%,#e34b2a)}
.tile{top:2731px;width:230px;height:131px;border:1.5px solid var(--tile-border);border-radius:6px;background:var(--white);display:flex;align-items:center;justify-content:center;font-family:'Lexend',sans-serif;font-weight:500;font-size:19px;color:var(--ink);text-align:center;padding:10px}
.news-band{left:0;top:2944px;width:1200px;height:648px;background:var(--band)}
.news-title{left:0;top:3007px;width:1200px;text-align:center;color:var(--white)}
.news-photo{left:97px;top:3092px;width:436px;height:436px;border-radius:50%;border:4px solid var(--white);background:linear-gradient(150deg,#dfe6ec,#c9453a 45%,#7a5a48 70%,#4f7ea0)}
.news-head{left:590px;top:3138px;font-family:'Lexend',sans-serif;font-weight:500;font-size:25px;color:var(--white)}
.news-date{left:590px;top:3190px;display:flex;align-items:center;gap:16px;font-family:'Lexend',sans-serif;font-weight:500;font-size:24px;color:var(--white)}
.news-text{left:592px;top:3262px;width:508px;text-align:justify;color:var(--white)}
.footer{left:0;top:3592px;width:1200px;height:80px;background:var(--footer);color:var(--white);font-size:19px;display:flex;align-items:center;justify-content:center}
</style>
</head>
<body>
<header class="abs hero">
</header>
<div class="abs brand-small"><span class="dot"></span>Inkvale Reads</div>
<div class="abs wordmark">Inkvale Reads</div>
<div class="abs hero-frame"></div>
<div class="abs photo hero-photo" role="img" aria-label="Artist with outstretched arm painting a vivid blue and orange abstract canvas"></div>

<section>
  <div class="abs shadow about-shadow"></div>
  <div class="abs about-photo" role="img" aria-label="Smiling artist in a black hat holding a brush and palette in her studio"></div>
  <div class="abs rule about-rule"></div>
  <h2 class="abs about-title">About Me</h2>
  <p class="abs body-copy about-text">Lorem ipsum dolor sit amet, consectetur adipiscing elit, sed do eiusmod tempor incididunt ut labore et dolore magna aliqua. Ut enim ad minim veniam, quis nostrud exercitation ullamco laboris nisi ut aliquip ex ea commodo consequat. Duis aute irure dolor in reprehenderit in voluptate velit esse cillum dolore eu fugiat nulla pariatur. Excepteur sint occaecat cupidatat non proident, sunt in culpa qui officia deserunt mollit anim id est laborum.Lorem ipsum dolor ameted consectetur adipiscing elit, sed do eiusmod tempor incididunt labored.</p>
</section>

<section>
  <div class="abs rule stories-rule"></div>
  <h2 class="abs stories-title">Short Stories</h2>
  <p class="abs body-copy stories-text">Lorem ipsum dolor sit amet, consectetur adipiscing elit, sed do eiusmod tempor incididunt ut labore et dolore magna aliqua. Ut enim ad minim veniam, quis nostrud exercitation ullamco laboris nisi ut aliquip ex ea commodo consequat. Duis aute irure dolor in reprehenderit in voluptate velit esse cillum dolore eu fugiat nulla pariatur. Excepteur sint occaecat cupidatat non proident, sunt in culpa qui officia deserunt mollit anim id est laborum.Lorem ipsum dolor ameted consectetur adipiscing elit, sed do eiusmod tempor incididunt labored.</p>
  <div class="abs shadow stories-shadow"></div>
  <div class="abs stories-photo" role="img" aria-label="Illustrated portrait surrounded by white lilies and orange flowers"></div>
</section>

<section>
  <div class="abs advice-band"></div>
  <h2 class="abs advice-title">Advice</h2>
  <p class="abs body-copy advice-text">Lorem ipsum dolor sit amet, consectetur adipiscing elit, sed do eiusmod tempor incididunt ut labore et dolore magna aliqua. Ut enim ad minim veniam, quis nostrud exercitation ullamco laboris nisi ut aliquip ex ea commodo consequat. Duis aute irure dolor in reprehenderit in voluptate velit esse cillum dolore eu fugiat nulla pariatur. Excepteur sint occaecat cupidatat non proident, sunt in culpa qui officia deserunt mollit anim id est laborum.</p>
  <div class="abs advice-photo" role="img" aria-label="Colourful collage illustration of a portrait with abstract flowers and shapes"></div>
</section>

<nav>
  <div class="abs tile" style="left:92px">Personal Pieces</div>
  <div class="abs tile" style="left:353px">I.V. on writing</div>
  <div class="abs tile" style="left:615px">The Writing Journey</div>
  <div class="abs tile" style="left:876px">News and Updates</div>
</nav>

<section>
  <div class="abs news-band"></div>
  <h2 class="abs news-title">Our News</h2>
  <div class="abs news-photo" role="img" aria-label="Close-up of a hand painting with a brush on a textured canvas"></div>
  <div class="abs news-head">Lorem ipsum dolor sit consectetur</div>
  <div class="abs news-date">
    <svg width="22" height="24" viewBox="0 0 22 24" aria-hidden="true">
      <rect x="1" y="3" width="20" height="20" rx="2" fill="none" stroke="#fff" stroke-width="2"/>
      <rect x="1" y="3" width="20" height="5" fill="#fff"/>
      <rect x="5" y="0" width="2" height="6" fill="#fff"/>
      <rect x="15" y="0" width="2" height="6" fill="#fff"/>
      <g fill="#fff"><rect x="4" y="11" width="3" height="3"/><rect x="9.5" y="11" width="3" height="3"/><rect x="15" y="11" width="3" height="3"/><rect x="4" y="16" width="3" height="3"/><rect x="9.5" y="16" width="3" height="3"/><rect x="15" y="16" width="3" height="3"/></g>
    </svg>
    <span>6.11.2024</span>
  </div>
  <p class="abs body-copy news-text">Lorem ipsum dolor sit amet, consectetur adipiscing elit, sed do eiusmod tempor incididunt ut labore et dolore magna aliqua. Ut enim ad minim veniam, quis nostrud exercitation ullamco laboris nisi ut aliquip ex ea commodo consequat. Duis aute irure dolor in reprehenderit in voluptate velit esse cillum dolore eu fugiat nulla pariatur. Excepteur sint occaecat cupidatat.</p>
</section>

<footer class="abs footer">© 2024 Copyrights&nbsp; Inkvale Reads All Rights Reserved.</footer>
</body>
</html>
```